Pre-workout label and Super Greens label for Vantora Nutrition Supplements

I need a label design for Club Vantora's 2 supplements. The first is a Pre-workout. The Pre-workout label needs to be 11.25 x 2.5 inches. This label will go on a black container. The second is a Super-Green. The Super-Green label should be 11.25 x 4.25 inches and will go on a white container. We have been selling these for a few years but the current labels are a little meh. I'd like something trendier and bolder. Must keep the Club Vantora branding. All the nurtition data must appear . I attached the current designs so you can know the flavors, nutrtional data etc. Thank you!
Updates

I can upload the Club Vantora logo! If anyone can tell me how to do that.

```html
<!DOCTYPE html>
<html lang="en">
<head>
<meta charset="utf-8">
<title>Vantora Nutrition – Pre-Workout and Super Green Labels</title>
<link rel="stylesheet" href="https://fonts.googleapis.com/css2?family=Anton&family=Roboto+Condensed:wght@400;700&display=swap">
<style>
  :root {
    --stage: #111214;
    --red: #d3202a;
    --red-deep: #8e1519;
    --navy: #0e1720;
    --green: #17a84a;
    --green-deep: #0f7f36;
    --green-line: #1f9a3f;
    --white: #ffffff;
    --silver: #d9dbdc;
    --ink: #111111;
  }
  html, body {
    margin: 0;
    width: 1200px;
    height: 881px;
    overflow: hidden;
    background: var(--stage);
  }
  .stage { position: relative; width: 1200px; height: 881px; }
  .label { position: absolute; display: block; }
  .label--preworkout { left: 124px; top: 355px; width: 370px; height: 280px; }
  .label--greens { left: 705px; top: 189px; width: 391px; height: 411px; }
  .title { font-family: "Anton", Impact, sans-serif; }
  .small { font-family: "Roboto Condensed", Arial, sans-serif; font-weight: 700; }
  .light { font-family: "Roboto Condensed", Arial, sans-serif; font-weight: 400; }
</style>
</head>
<body>
<main class="stage">

  <!-- Pre-workout label -->
  <svg class="label label--preworkout" viewBox="0 0 370 280" aria-label="Vantora Nutrition Pre-Workout label">
    <defs>
      <linearGradient id="pw-red" x1="0" y1="0" x2="1" y2="1">
        <stop offset="0" stop-color="var(--red)"/>
        <stop offset="1" stop-color="var(--red-deep)"/>
      </linearGradient>
    </defs>
    <rect class="pw-top" width="370" height="280" fill="url(#pw-red)"/>
    <polygon class="pw-rule" points="0,128 370,56 370,62 0,134" fill="var(--navy)"/>
    <polygon class="pw-flavour-band" points="0,181 370,112 370,128 0,197" fill="var(--navy)"/>
    <polygon class="pw-lower" points="0,203 370,133 370,256 0,256" fill="var(--navy)"/>
    <rect class="pw-footer" y="256" width="370" height="24" fill="var(--red)"/>

    <g class="pw-brandmark">
      <rect x="155" y="25" width="9" height="9" fill="var(--white)"/>
      <text x="168" y="34" class="small" font-size="11" fill="var(--white)">VANTORA</text>
    </g>

    <g transform="rotate(-10.8 185 120)">
      <text x="183" y="92" class="small" font-size="13" fill="var(--white)" text-anchor="middle" letter-spacing="0.5">VANTORA NUTRITION</text>
      <text x="185" y="134" class="title" font-size="40" fill="var(--white)" text-anchor="middle">PRE-WORKOUT</text>
      <text x="180" y="160" class="small" font-size="9" fill="var(--white)" text-anchor="middle" letter-spacing="0.6">WATERMELON SUGAR</text>
    </g>

    <g class="pw-benefits" fill="var(--white)">
      <g transform="translate(120 206)">
        <path d="M-13,-13 h26 v19 l-13,8 l-13,-8z" fill="var(--red)" stroke="var(--white)" stroke-width="1.5"/>
        <path d="M2,-10 l-7,9 h5 l-3,8 l8,-10 h-5z"/>
      </g>
      <g transform="translate(187 206)">
        <path d="M-13,-13 h26 v19 l-13,8 l-13,-8z" fill="var(--red)" stroke="var(--white)" stroke-width="1.5"/>
        <path d="M0,-10 l7,7 h-4 v9 h-6 v-9 h-4z"/>
      </g>
      <g transform="translate(254 206)">
        <path d="M-13,-13 h26 v19 l-13,8 l-13,-8z" fill="var(--red)" stroke="var(--white)" stroke-width="1.5"/>
        <rect x="-9" y="-4" width="3" height="8"/><rect x="6" y="-4" width="3" height="8"/>
        <rect x="-6" y="-1" width="12" height="2"/>
      </g>
      <text x="120" y="234" class="small" font-size="8" text-anchor="middle">ENERGY*</text>
      <text x="120" y="245" class="light" font-size="7.5" text-anchor="middle">(Caffeine)</text>
      <text x="187" y="234" class="small" font-size="8" text-anchor="middle">PERFORMANCE*</text>
      <text x="187" y="245" class="light" font-size="7.5" text-anchor="middle">(Beta-alanine)</text>
      <text x="254" y="234" class="small" font-size="8" text-anchor="middle">STRENGTH*</text>
      <text x="254" y="245" class="light" font-size="7.5" text-anchor="middle">(Creatine)</text>
    </g>

    <g class="pw-footer-text small" font-size="7.5" fill="var(--white)" text-anchor="middle">
      <text x="113" y="271">DIETARY SUPPLEMENT</text>
      <text x="253" y="271">30 SERVINGS 240g (8.5oz)</text>
    </g>
  </svg>

  <!-- Super Green label -->
  <svg class="label label--greens" viewBox="0 0 391 411" aria-label="Vantora Nutrition Super Green label">
    <defs>
      <linearGradient id="sg-silver" x1="0" y1="0" x2="1" y2="0">
        <stop offset="0" stop-color="var(--silver)"/>
        <stop offset="0.5" stop-color="var(--white)"/>
        <stop offset="1" stop-color="var(--silver)"/>
      </linearGradient>
      <linearGradient id="sg-green" x1="0" y1="0" x2="1" y2="1">
        <stop offset="0" stop-color="var(--green)"/>
        <stop offset="1" stop-color="var(--green-deep)"/>
      </linearGradient>
    </defs>
    <rect class="sg-top" width="391" height="411" fill="url(#sg-silver)"/>
    <polygon class="sg-rule" points="0,160 391,80 391,85 0,165" fill="var(--green-line)"/>
    <polygon class="sg-flavour-band" points="0,224 391,147 391,166 0,243" fill="var(--navy)"/>
    <polygon class="sg-lower" points="0,249 391,171 391,372 0,372" fill="url(#sg-green)"/>
    <rect class="sg-footer" y="372" width="391" height="39" fill="var(--navy)"/>

    <g class="sg-brandmark">
      <rect x="163" y="45" width="10" height="10" fill="var(--red)"/>
      <text x="177" y="55" class="small" font-size="12" fill="var(--ink)">VANTORA</text>
    </g>

    <g transform="rotate(-11.3 195 150)">
      <text x="196" y="114" class="small" font-size="16" fill="var(--ink)" text-anchor="middle" letter-spacing="0.6">VANTORA NUTRITION</text>
      <text x="188" y="170" class="title" font-size="52" fill="var(--ink)" text-anchor="middle">SUPER GREEN</text>
      <text x="190" y="198" class="small" font-size="11" fill="var(--white)" text-anchor="middle" letter-spacing="0.6">APPLE CINNAMON</text>
    </g>

    <g class="sg-benefits" fill="var(--white)">
      <g transform="translate(97 283)">
        <path d="M-16,-16 h32 v23 l-16,10 l-16,-10z" fill="var(--red)" stroke="var(--white)" stroke-width="1.5"/>
        <path d="M-10,-2 a4,4 0 1 1 0,0.1 M10,-2 a4,4 0 1 1 0,0.1" fill="none"/>
        <circle cx="-5" cy="-2" r="5" fill="none" stroke="var(--white)" stroke-width="2.5"/>
        <circle cx="5" cy="-2" r="5" fill="none" stroke="var(--white)" stroke-width="2.5"/>
      </g>
      <g transform="translate(184 283)">
        <path d="M-16,-16 h32 v23 l-16,10 l-16,-10z" fill="var(--red)" stroke="var(--white)" stroke-width="1.5"/>
        <path d="M-2,-11 v5 c8,0 9,12 0,12 c-4,0 -6,2 -6,5" fill="none" stroke="var(--white)" stroke-width="1.6"/>
      </g>
      <g transform="translate(271 283)">
        <path d="M-16,-16 h32 v23 l-16,10 l-16,-10z" fill="var(--red)" stroke="var(--white)" stroke-width="1.5"/>
        <path d="M0,6 l-8,-8 a4.5,4.5 0 0 1 8,-5 a4.5,4.5 0 0 1 8,5z"/>
      </g>
      <text x="97" y="323" class="small" font-size="10.5" text-anchor="middle" letter-spacing="0.8">DETOX</text>
      <text x="97" y="335" class="light" font-size="8" text-anchor="middle">BODY*</text>
      <text x="184" y="322" class="small" font-size="10.5" text-anchor="middle" letter-spacing="0.8">PROMOTE</text>
      <text x="184" y="336" class="small" font-size="10.5" text-anchor="middle" letter-spacing="0.8">HEALTHY</text>
      <text x="184" y="348" class="light" font-size="8" text-anchor="middle">DIGESTION*</text>
      <text x="273" y="322" class="small" font-size="10.5" text-anchor="middle">SUPPORT</text>
      <text x="273" y="334" class="light" font-size="8" text-anchor="middle">IMMUNITY*</text>
    </g>

    <g class="sg-footer-text small" font-size="8.5" fill="var(--white)" text-anchor="middle" letter-spacing="0.4">
      <text x="113" y="395">DIETARY SUPPLEMENT</text>
      <text x="271" y="395">30 SERVINGS 270g (9.5oz)</text>
    </g>
  </svg>

</main>
</body>
</html>
```